Website for data analytics startup

I have a landing page up at http://vantiq.io I need to expand this into a basic company website. I want something similar to this design: http://fetchlayout.com/samples/slider/

I need HTML and CSS for each of the designs, once they are approved. I need the following pages: home page, product, team, blog, and a design for the container of our demo application.

Our logo is attached and also available here: https://files.cloudvessel.com/vantiq.public/LOGO-colour.png I would like the website branding to match the logo.

I need a blog design with CSS that works with Pindle.

Our app can be seen at http://demo.vantiq.io Please don't change the look of the network graph itself, only the surrounding content.

For CSS, I want you to use Scaffolder or Groundwork as the starting point.

Target Market(s)

Sales and marketing, strategy

Industry/Entity Type

It Company

Coding

Coded - Design and coding required

Number of Pages Required

4 page

Font styles to use
Serif
Sans Serif

Requirements
Must have
• Clean, healthy appeal. Must work well with our logo. Blog page must integrate with Pindle easily. Must use Scaffolder or Groundwork for the starting point of the HTML/CSS.
Should not have
• Ugly crap, flash looking design. NO FLASH.

```html
<!DOCTYPE html>
<html lang="en">
<head>
<meta charset="utf-8">
<title>Orvalo – Data Analytics</title>
<link href="https://fonts.googleapis.com/css2?family=Raleway:wght@300;400;500;600;700&display=swap" rel="stylesheet">
<style>
:root{
  --sky:#6ecbf3;
  --green:#7bc142;
  --navy:#0b4a66;
  --ink:#3f4a50;
  --muted:#8a9398;
  --card:#f4f4f4;
  --white:#ffffff;
}
*{box-sizing:border-box;margin:0;padding:0}
html,body{width:696px;height:1200px;overflow:hidden}
body{position:relative;font-family:'Raleway',sans-serif;color:var(--ink);background:var(--white)}

/* header */
.site-header{position:absolute;left:0;top:0;width:696px;height:56px;background:var(--white)}
.brand{position:absolute;left:64px;top:18px;display:flex;align-items:center;gap:5px;font-weight:700;font-size:17px;color:var(--navy)}
.brand-dot{width:7px;height:7px;border-radius:50%;background:var(--green)}
.main-nav{position:absolute;right:64px;top:24px;display:flex;gap:17px;font-size:8.5px;color:#333}

/* hero */
.hero{position:absolute;left:0;top:56px;width:696px;height:276px;background:var(--sky)}
.hero-art{position:absolute;left:262px;top:34px;width:172px;height:134px;border-radius:6px;background:linear-gradient(180deg,#8fd6f5,#5fbfe8)}
.hero-floor{position:absolute;left:50px;top:172px;width:586px;height:2px;background:#62bde6}
.slider-arrow{position:absolute;top:126px;width:18px;height:26px}
.slider-arrow.prev{left:32px}
.slider-arrow.next{right:32px}
.hero-title{position:absolute;left:0;width:696px;top:184px;text-align:center;font-weight:300;font-size:18px;color:var(--white)}
.btn-demo{position:absolute;left:270px;top:221px;width:156px;height:26px;border-radius:3px;background:var(--green);color:var(--white);font-size:8px;font-weight:600;display:flex;align-items:center;justify-content:center}

/* features */
.section-title{position:absolute;left:0;width:696px;top:364px;text-align:center;font-size:18px;font-weight:400;color:var(--navy)}
.feature{position:absolute;top:403px;width:180px;height:176px;background:var(--card);text-align:center}
.feature svg{position:absolute;left:50%;top:20px;transform:translateX(-50%)}
.feature h3{position:absolute;top:63px;width:100%;font-size:9.5px;font-weight:500;color:#333}
.feature p{position:absolute;left:8px;right:8px;top:84px;font-size:7px;line-height:12px;font-weight:300;color:var(--muted)}
.btn-more{position:absolute;left:57px;top:147px;width:66px;height:20px;border:1.5px solid var(--sky);border-radius:5px;font-size:7px;font-weight:500;color:#333;display:flex;align-items:center;justify-content:center;background:var(--white)}

/* contact band */
.cta{position:absolute;left:0;top:613px;width:696px;height:225px;background:var(--green);color:var(--white)}
.cta h2{position:absolute;top:24px;width:100%;text-align:center;font-size:16px;font-weight:700}
.cta-lead{position:absolute;top:52px;width:100%;text-align:center;font-size:8.5px}
.field{position:absolute;background:var(--white);font-size:6.5px;color:#bbb;padding:8px 6px}
.btn-callback{position:absolute;left:355px;top:165px;width:95px;height:23px;background:var(--sky);font-size:7px;font-weight:700;display:flex;align-items:center;justify-content:center}
.privacy{position:absolute;left:456px;top:172px;font-size:7px;font-weight:600}

/* app promo */
.promo-brand{position:absolute;left:0;width:696px;top:888px;display:flex;justify-content:center;align-items:center;gap:7px;font-size:28px;font-weight:700;color:var(--navy)}
.promo-brand .brand-dot{width:12px;height:12px}
.promo-text{position:absolute;left:0;width:696px;top:931px;text-align:center;font-size:9px;color:#444}
.btn-app{position:absolute;left:279px;top:962px;width:138px;height:29px;border-radius:3px;background:var(--green);color:var(--white);font-size:12px;font-weight:500;display:flex;align-items:center;justify-content:center}

/* footer */
.site-footer{position:absolute;left:0;top:1027px;width:696px;height:173px;background:var(--navy);color:var(--white);font-size:7.2px}
.foot-col{position:absolute;top:29px;line-height:15px}
.social{position:absolute;left:549px;display:flex;align-items:center;width:82px;justify-content:space-between}
.social-circle{width:21px;height:21px;border-radius:50%}
.copyright{position:absolute;top:150px;width:100%;text-align:center}
</style>
</head>
<body>

<header class="site-header">
  <div class="brand"><span class="brand-dot"></span>orvalo</div>
  <nav class="main-nav"><span>About</span><span>Services</span><span>Contact</span></nav>
</header>

<section class="hero">
  <div class="hero-art" role="img" aria-label="Illustration of a presenter pointing at a board of charts"></div>
  <div class="hero-floor"></div>
  <svg class="slider-arrow prev" viewBox="0 0 18 26"><polyline points="14,3 4,13 14,23" fill="none" stroke="#fff" stroke-width="3.5"/></svg>
  <svg class="slider-arrow next" viewBox="0 0 18 26"><polyline points="4,3 14,13 4,23" fill="none" stroke="#fff" stroke-width="3.5"/></svg>
  <h1 class="hero-title">Orvalo Maps Markets to Drive Sales and Marketing</h1>
  <div class="btn-demo">SIGN UP NOW FOR A FREE DEMO</div>
</section>

<h2 class="section-title">Data Analytics</h2>

<article class="feature" style="left:64px">
  <svg width="28" height="32" viewBox="0 0 28 32"><path d="M2 2h24v14c0 8-6 12-12 15C8 28 2 24 2 16z" fill="#7bc142"/><path d="M9 7h10v9c0 5-3 7-5 9-2-2-5-4-5-9z" fill="#fff"/></svg>
  <h3>Data Visualisation</h3>
  <p>Lorem Ipsum is simply dummy text of the printing and typesetting industry. Lorem Ipsum has been the industry's standard dummy text ever since the 1500s, when an unknown printer.</p>
  <div class="btn-more">Read More</div>
</article>

<article class="feature" style="left:257px">
  <svg width="42" height="32" viewBox="0 0 42 32"><path d="M2 0v30h40" fill="none" stroke="#7bc142" stroke-width="3"/><rect x="9" y="18" width="5" height="10" fill="#7bc142"/><rect x="17" y="12" width="5" height="16" fill="#7bc142"/><rect x="25" y="15" width="5" height="13" fill="#7bc142"/><rect x="33" y="6" width="5" height="22" fill="#7bc142"/></svg>
  <h3>Business Intelligence</h3>
  <p>Lorem Ipsum is simply dummy text of the printing and typesetting industry. Lorem Ipsum has been the industry's standard dummy text ever since the 1500s, when an unknown printer.</p>
  <div class="btn-more">Read More</div>
</article>

<article class="feature" style="left:452px">
  <svg width="32" height="36" viewBox="0 0 32 36"><g fill="#7bc142"><ellipse cx="16" cy="5" rx="15" ry="5"/><rect x="1" y="9" width="30" height="7" rx="3.5"/><rect x="1" y="18" width="30" height="7" rx="3.5"/><rect x="1" y="27" width="30" height="8" rx="4"/></g></svg>
  <h3>Big Data</h3>
  <p>Lorem Ipsum is simply dummy text of the printing and typesetting industry. Lorem Ipsum has been the industry's standard dummy text ever since the 1500s, when an unknown printer.</p>
  <div class="btn-more">Read More</div>
</article>

<section class="cta">
  <h2>Get Started Now</h2>
  <p class="cta-lead">As soon as you contact our expert team, this will be the only form you have to fill in!</p>
  <div class="field" style="left:64px;top:86px;width:276px;height:23px">Name</div>
  <div class="field" style="left:64px;top:126px;width:276px;height:23px">E-Mail</div>
  <div class="field" style="left:64px;top:165px;width:276px;height:23px">Phone</div>
  <div class="field" style="left:355px;top:86px;width:277px;height:63px">Message</div>
  <div class="btn-callback">REQUEST A CALLBACK</div>
  <div class="privacy">100% Privacy Guaranteed</div>
</section>

<div class="promo-brand"><span class="brand-dot"></span>orvalo</div>
<p class="promo-text">Neque porro quisquam est qui dolorem ipsum quia dolor sit amet, consectetur, adipisci velit.</p>
<div class="btn-app">Download Our App</div>

<footer class="site-footer">
  <div class="foot-col" style="left:65px">About<br>Services<br>Contact</div>
  <div class="foot-col" style="left:177px">Terms &amp; Conditions<br>Privacy Policy<br>Disclaimer<br>Legal Notice</div>
  <div class="foot-col" style="left:305px">Help<br>Downoads<br>FAQ's<br>Customer Support</div>
  <div class="foot-col" style="left:403px">Werkstattbüro Nord<br>Lindenweg 42b<br>20095 Hafenstadt<br>Germany<br>Telephone: +49 40 55501234<br>E-mail: hallo@werkstattnord.de</div>
  <div class="social" style="top:26px"><span>Circlehub</span><span class="social-circle" style="background:#3a5a9c"></span></div>
  <div class="social" style="top:65px"><span>Chirpline</span><span class="social-circle" style="background:#4ec0e4"></span></div>
  <div class="social" style="top:103px"><span>Worknet</span><span class="social-circle" style="background:#1a7bb5"></span></div>
  <div class="copyright">© 2015 Company Name, All Rights Reserved</div>
</footer>

</body>
</html>
```